International Tour Operator Needs A New Brochure

We are a newly set up small tour operator focusing on personal tailor made honeymoons for our guests.

We would like to see our logo incorporated into the brochure design as well as our website: mirabelfenwickjourneys.co.uk; our e-mail address tobias@mirabelfenwickjourneys.co.uk; and our mobile number +44 (0)7812469035.

Where as the logo is required, the content in the word document does not have to be used/included. It is there to provide background information on what we do.

The final design should be professional, clear/not crowded, attention grabbing and fit the industry and target segment (brides and grooms).

Target Market(s)

Brides and grooms

Industry/Entity Type

Industry

Colors

Designer to choose colors to be used in the design.

Requirements
Must have
• Logo
Nice to have
• Some content from the word document

```html
<!DOCTYPE html>
<html lang="en">
<head>
<meta charset="utf-8">
<title>Mirabel Fenwick Journeys – Our Honeymoons</title>
<link rel="stylesheet" href="https://fonts.googleapis.com/css2?family=Questrial&family=Arimo:ital,wght@0,400;0,700;1,700&display=swap">
<style>
  :root {
    --page-bg: #e6e6e6;
    --paper: #ffffff;
    --leaf: #8cc43c;
    --forest: #3d6b5c;
    --ink: #555a58;
    --ink-strong: #2f3a36;
    --fold: #e2e2e2;
    --sunset: #e0612a;
    --sea: #6fbcd6;
    --sand: #e9dcc3;
    --stone: #b27a4a;
    --sky: #8fc3de;
    --rose: #b7323b;
  }
  * { box-sizing: border-box; margin: 0; padding: 0; }
  html, body { width: 1200px; height: 800px; overflow: hidden; }
  body {
    background: var(--page-bg);
    font-family: "Arimo", Arial, sans-serif;
    color: var(--ink);
    display: flex; align-items: center; justify-content: center;
  }
  .brochure {
    width: 1080px; height: 760px;
    background: var(--paper);
    display: grid; grid-template-columns: repeat(3, 1fr);
    box-shadow: 0 6px 24px rgba(0,0,0,.12);
  }
  .panel {
    padding: 26px 26px 20px;
    border-right: 1px solid var(--fold);
    display: flex; flex-direction: column; gap: 18px;
  }
  .panel:last-child { border-right: none; }
  .panel--intro { padding-left: 0; padding-right: 0; gap: 14px; }

  .brand {
    height: 190px;
    display: flex; align-items: center; justify-content: center; gap: 10px;
  }
  .brand__dot { width: 14px; height: 14px; border-radius: 50%; background: var(--leaf); }
  .brand__name {
    font-family: "Questrial", sans-serif;
    font-size: 30px; line-height: 1.05; color: var(--forest);
    text-align: center;
  }
  .title-band {
    background: var(--forest); color: #fff;
    width: 86%; height: 50px;
    display: flex; align-items: center; padding-left: 26px;
    font-family: "Questrial", sans-serif; font-size: 27px;
  }
  .intro { padding: 0 26px; display: flex; flex-direction: column; gap: 10px; }
  .intro__lead { color: var(--leaf); font-weight: 700; font-style: italic; font-size: 13px; }
  .intro p { font-size: 11px; line-height: 1.35; }
  .panel--intro .region { padding: 0 26px; margin-top: 14px; }

  .region { display: flex; flex-direction: column; gap: 8px; }
  .region__bar {
    background: var(--leaf); color: #fff;
    font-family: "Questrial", sans-serif; font-size: 17px;
    height: 28px; display: flex; align-items: center; padding-left: 10px;
  }
  .region__body { font-size: 10.5px; line-height: 1.38; text-align: justify; }
  .region__body p + p { margin-top: 7px; }
  .photo {
    float: left; width: 118px; height: 76px; margin: 2px 10px 4px 0;
  }
  .photo--sunset { background: linear-gradient(180deg, #f7a03a, var(--sunset) 60%, #3a1a10); }
  .photo--beach { background: linear-gradient(180deg, var(--sky), var(--sea) 50%, var(--sand) 55%); }
  .photo--rome { background: linear-gradient(180deg, #5f9fd2, var(--stone) 55%, #8a5a33); }
  .photo--bridge { background: linear-gradient(180deg, #b8d7e8, #c14a33 60%, #4f7d8f); }
  .photo--palms { background: linear-gradient(180deg, #79b6e3, #3f8a3a 60%, #d9d2b0); }
  .photo--shore { background: linear-gradient(180deg, #9ccbe8, #5aaed0 45%, var(--sand) 55%); }
  .photo--petals { background: linear-gradient(135deg, #d9b7a3, var(--rose) 60%, #6e1b22); }
  .keys { clear: both; font-size: 11px; }
  .keys__label { color: var(--leaf); font-weight: 700; }
  .keys__list { color: var(--ink-strong); font-weight: 700; line-height: 1.3; }
</style>
</head>
<body>
<main class="brochure">

  <section class="panel panel--intro">
    <header class="brand">
      <span class="brand__dot"></span>
      <span class="brand__name">Mirabel Fenwick<br>Journeys</span>
    </header>
    <h1 class="title-band">Our Honeymoons</h1>
    <div class="intro">
      <p class="intro__lead">Let us help you with your honeymoon...</p>
      <p>Deciding where to go on your honeymoon is an important decision, one we intend to make once.</p>
      <p>Whether it's an exotic escape to a pristine secluded beach, a luxurious safari, a cosmopolitan mecca or you have not quite decided yet contact us to discuss!</p>
      <p>Benefit from our expertise, consumer protection&amp; fantastic rates...</p>
    </div>
    <article class="region">
      <h2 class="region__bar">Asia</h2>
      <div class="region__body">
        <div class="photo photo--petals" role="img" aria-label="Photo of a bride relaxing in a bath of rose petals"></div>
        <p>Friendly people, beautiful beaches and a rich cultural heritage awaits you in Asia. If you are willing to spend two days in transit Asia is a great venue.</p>
        <p>You are sure to enjoy the delights that the Orient has to offer if you like amazing beaches, exploring new cultures and getting pampered.</p>
      </div>
      <p class="keys"><span class="keys__label">Key Destinations:</span><br><span class="keys__list">Maldvies, Sri Lanka, Japan, Thailand &amp; Bali</span></p>
    </article>
  </section>

  <section class="panel">
    <article class="region">
      <h2 class="region__bar">Sub Saharan Africa</h2>
      <div class="region__body">
        <div class="photo photo--sunset" role="img" aria-label="Photo of elephants silhouetted against an African sunset"></div>
        <p>Africa is the ideal destination for the connoisseur with abundant wildlife, gorgeous beaches, adventure sports and renowned vineyards.</p>
        <p>If you are looking for something extraordinary &amp; are not worried about getting a bit dusty Africa is the destination for you.</p>
      </div>
      <p class="keys"><span class="keys__label">Key Destinations:</span><br><span class="keys__list">Mauritius, Botswana, Namibia, Madagascar, South Africa, Zambia, Tanzania &amp; Kenya.</span></p>
    </article>
    <article class="region">
      <h2 class="region__bar">North Africa &amp; Middle East</h2>
      <div class="region__body">
        <div class="photo photo--beach" role="img" aria-label="Photo of two sun loungers on a white beach"></div>
        <p>If you are not looking to travel far and are looking for a beach based luxury holiday North Africa and The Middle East is a great choice.</p>
        <p>Vibrant marketplaces, friendly people &amp; pristine beaches await you.</p>
        <p>Many people have been put off by recent instability in the region but this has not affected every destination. By working with us we can help you select the ideal holiday in peace.</p>
      </div>
      <p class="keys"><span class="keys__label">Key Destinations:</span><br><span class="keys__list">Abhu Dhabi, Egypt, Morocco, Doha &amp; Algeria</span></p>
    </article>
    <article class="region">
      <h2 class="region__bar">Europe</h2>
      <div class="region__body">
        <div class="photo photo--rome" role="img" aria-label="Photo of the Colosseum in Rome under a blue sky"></div>
        <p>If you are looking for short travel times, great architecture and delightful cuisine Europe may be the destination for you.</p>
        <p>These locations are renowned as some of the most romantic in the world and we can help book you in to some of the most prestigious at a reduced cost.</p>
      </div>
      <p class="keys"><span class="keys__label">Key Destinations:</span><br><span class="keys__list">Paris, Rome, The Alps, Greece, Spain, Vienna, Venice, Istanbul &amp; Tuscany</span></p>
    </article>
  </section>

  <section class="panel">
    <article class="region">
      <h2 class="region__bar">North America</h2>
      <div class="region__body">
        <div class="photo photo--bridge" role="img" aria-label="Photo of a red suspension bridge over a bay"></div>
        <p>Always a favourite for those looking for the cosmopolitan experience or a great rail journey across beautiful valleys and glistening peaks, North America is a great option for those with the money.</p>
        <p>Most people opt for a shorter honeymoon in North America to compensate for higher costs but we can ensure you get the best quality accommodation for a fair price.</p>
      </div>
      <p class="keys"><span class="keys__label">Key Destinations:</span><br><span class="keys__list">New York Quebec, British Columbal, San Fransisco, Cancun &amp; Las Vegas.</span></p>
    </article>
    <article class="region">
      <h2 class="region__bar">Central America</h2>
      <div class="region__body">
        <div class="photo photo--palms" role="img" aria-label="Photo of palm trees around a tropical resort pool"></div>
        <p>Central America offers tropical sun and pristine coastline to those willing to travel. Honeymoon locations are firmly established in the area although many are expensive.</p>
        <p>Let us help you get past the costs and ensure you get the most from your once in a lifetime experience.</p>
      </div>
      <p class="keys"><span class="keys__label">Key Destinations:</span><br><span class="keys__list">Cancun, Bahamas, St Lucia, Belize, Costa Rica, Aruba, Dominica, Jamaica, Anguilla &amp; Antigua</span></p>
    </article>
    <article class="region">
      <h2 class="region__bar">South America</h2>
      <div class="region__body">
        <div class="photo photo--shore" role="img" aria-label="Photo of a thatched parasol and loungers on a sandy beach"></div>
        <p>South America is still developing as a honeymoon location and there is the opportunity to get a great deal for an unforgettable experience.</p>
        <p>There is a great deal of linguistic and cultural heritage in the region for the budding adventurer to sample.</p>
      </div>
      <p class="keys"><span class="keys__label">Key Destinations:</span><br><span class="keys__list">Cartagena, Tayrona National Park, Machu Picchu, Easter Island, Iguassu Falls, The Amazon, The Galapagos, Rio de Janeiro &amp; Buenos Aries</span></p>
    </article>
  </section>

</main>
</body>
</html>
```